Stationery Design Project

Minimal Design. Black and White Colours Only.
Need Business Card
With Compliments slip
Letterhead
A4 Folder

Target Market(s)

Luxury architectual designed home owners

Industry/Entity Type

Business

Requirements
Must have
• Black and White colours only. Suggest some good textured stock for business card for future printing. try to use font that is used in my logo our some other minimal modern font.

```html
<!DOCTYPE html>
<html lang="en">
<head>
<meta charset="utf-8">
<title>Kelvar Estates – Business Card</title>
<link rel="stylesheet" href="https://fonts.googleapis.com/css2?family=Arimo:wght@400;700&family=Roboto+Condensed:wght@400;700&display=swap">
<style>
  :root {
    --backdrop: #b3b3b3;
    --ink: #1a1a1a;
    --band: #333333;
    --paper: #ffffff;
    --mist: #e6e6e6;
    --rule: #aaaaaa;
    --text: #222222;
    --muted: #8a8a8a;
    --light-text: #e8e8e8;
  }
  * { margin: 0; padding: 0; box-sizing: border-box; }
  html, body { width: 992px; height: 1200px; overflow: hidden; background: var(--backdrop); }
  .canvas { position: relative; width: 992px; height: 1200px; font-family: "Arimo", Arial, sans-serif; }
  .shapes { position: absolute; inset: 0; }
  .brand-mark { position: absolute; background: var(--ink); }
  .brand-name {
    position: absolute; font-family: "Arimo", Arial, sans-serif; font-weight: 700;
    color: var(--ink); text-align: center; letter-spacing: 0.5px; line-height: 1.1;
  }
  .front .brand-mark { left: 677px; top: 200px; width: 60px; height: 60px; }
  .front .brand-name { left: 520px; width: 374px; top: 385px; font-size: 44px; }
  .back .brand-mark { left: 735px; top: 820px; width: 50px; height: 50px; }
  .back .brand-name { left: 560px; width: 400px; top: 945px; font-size: 36px; }
  .holder-name {
    position: absolute; left: 133px; top: 640px; font-family: "Roboto Condensed", "Arial Narrow", sans-serif;
    font-weight: 700; font-size: 40px; color: var(--light-text); letter-spacing: 0.5px;
  }
  .holder-role {
    position: absolute; left: 133px; top: 696px; font-family: "Roboto Condensed", "Arial Narrow", sans-serif;
    font-size: 21px; color: var(--light-text);
  }
  .contact { position: absolute; left: 133px; font-size: 20px; color: var(--text); line-height: 24px; }
  .contact .label { color: var(--muted); }
</style>
</head>
<body>
<div class="canvas">
  <svg class="shapes" width="992" height="1200" viewBox="0 0 992 1200" aria-hidden="true">
    <!-- front -->
    <rect x="22" y="33" width="945" height="553" fill="var(--ink)" stroke="#000" stroke-width="3"/>
    <path d="M445,35 Q345,310 445,585 L966,585 L966,35 Z" fill="var(--paper)"/>
    <path d="M24,216 L540,216 Q572,310 540,403 L24,403 Z" fill="var(--band)"/>
    <path d="M966,216 L878,216 Q846,310 878,403 L966,403 Z" fill="var(--band)"/>
    <!-- back -->
    <rect x="22" y="612" width="945" height="556" fill="var(--ink)" stroke="#000" stroke-width="3"/>
    <line x1="545" y1="614" x2="468" y2="750" stroke="#262626" stroke-width="2"/>
    <line x1="468" y1="1030" x2="545" y2="1166" stroke="#262626" stroke-width="2"/>
    <circle cx="760" cy="890" r="195" fill="var(--mist)"/>
    <rect x="553" y="750" width="412" height="280" fill="var(--mist)"/>
    <rect x="25" y="750" width="523" height="280" fill="var(--paper)"/>
    <rect x="548" y="750" width="5" height="280" fill="var(--rule)"/>
    <!-- profile placeholder -->
    <rect x="58" y="650" width="54" height="64" fill="#e6e6e6" role="img" aria-label="Profile silhouette icon"/>
    <!-- phone icon -->
    <g fill="var(--text)">
      <path d="M86,806 Q97,798 108,806 L108,810 L103,810 L102,807 Q97,805 92,807 L91,810 L86,810 Z"/>
      <rect x="89" y="811" width="16" height="9" rx="1"/>
    </g>
    <!-- envelope icon -->
    <g fill="none" stroke="var(--text)" stroke-width="2">
      <rect x="86" y="865" width="22" height="14"/>
      <path d="M86,865 L97,874 L108,865 M86,879 L94,871 M108,879 L100,871"/>
    </g>
    <!-- globe icon -->
    <g fill="none" stroke="var(--text)" stroke-width="2">
      <circle cx="97" cy="913" r="10"/>
      <ellipse cx="97" cy="913" rx="4.5" ry="10"/>
      <path d="M87,913 L107,913 M89,907 L105,907 M89,919 L105,919"/>
    </g>
    <!-- home icon -->
    <g fill="var(--text)">
      <path d="M85,966 L97,955 L109,966 L106,966 L97,958 L88,966 Z"/>
      <path d="M90,965 L97,959 L104,965 L104,974 L99,974 L99,968 L95,968 L95,974 L90,974 Z"/>
    </g>
  </svg>

  <section class="front">
    <div class="brand-mark"></div>
    <div class="brand-name">KELVAR<br>ESTATES</div>
  </section>

  <section class="back">
    <div class="holder-name">MARCUS HALE</div>
    <div class="holder-role">Managing Director</div>
    <div class="contact" style="top:790px">61 400 555 012 <span class="label">Mobile</span><br>61 7 3000 0199 <span class="label">Phone</span></div>
    <div class="contact" style="top:857px">mhale@kelvarestates.com</div>
    <div class="contact" style="top:900px">www.kelvarestates.com</div>
    <div class="contact" style="top:943px">Level 12, 40 Harbour Rd<br>Brisbane QLD 4000 Australia</div>
    <div class="brand-mark"></div>
    <div class="brand-name">KELVAR ESTATES</div>
  </section>
</div>
</body>
</html>
```